Networking Events Calendar/Diary

We need a responsive website that can act as both an online diary/calendar and a resource for community and networking events similar to mingleroundsplaza.com (we do not want a clone, but one with similar functionality). We need to be able to host adverts, have a client area for clients to add their own events to the diary. This needs to have the functionality that clients have to pay to add recurring events. Some integration would be useful so that if a clients already has their own online diary on their website then using an API possibly to also add that event into our online diary

Industry/Entity Type

Events

Coding

Coded - Design and coding required

Number of Pages Required

5+ page

Requirements
Must have
• My project must have a calendar area, space for ads, be responsive and easily viewable on mobile. A subscribers area for clients and a way to purchase premium status so that premium events are highlighted.

```html
<!DOCTYPE html>
<html lang="en">
<head>
<meta charset="utf-8">
<title>Rounds Plaza Diary</title>
<link rel="stylesheet" href="https://fonts.googleapis.com/css2?family=Open+Sans:wght@400;600;700&family=Raleway:wght@400;500;600;700&display=swap">
<style>
:root{
  --navy:#123c69;
  --navy-dark:#0e3259;
  --navy-light:#245b92;
  --orange:#f5a01a;
  --orange-dark:#e08e0c;
  --ink:#1f2a36;
  --text:#5e646b;
  --muted:#8a9096;
  --line:#e1e4e8;
  --panel:#f1f2f3;
  --hero-panel:rgba(52,57,64,.92);
  --white:#ffffff;
}
*{box-sizing:border-box;margin:0;padding:0}
html,body{width:1200px;height:3543px;overflow:hidden;background:var(--white)}
body{font-family:"Open Sans",Arial,sans-serif;color:var(--text);position:relative}
a{color:inherit;text-decoration:none}

/* header */
.site-header{position:absolute;left:0;top:0;width:1200px;height:118px}
.brand{position:absolute;left:99px;top:20px}
.brand-name{font-family:"Open Sans",Arial,sans-serif;font-weight:600;font-size:38px;color:var(--navy);line-height:1.1}
.brand-tag{font-size:12.5px;color:var(--ink);margin-top:12px}
.search-btn{position:absolute;left:585px;top:49px;width:34px;height:34px;border-radius:50%;background:#e6e8ea}
.top-link{position:absolute;top:59px;font-size:12px;color:var(--ink);white-space:nowrap}
.login{position:absolute;left:1006px;top:48px;width:95px;height:36px;background:var(--orange);color:#fff;font-size:14px;font-weight:700;text-align:center;line-height:36px;border-radius:2px}

.main-nav{position:absolute;left:0;top:118px;width:1200px;height:59px;background:var(--navy)}
.main-nav ul{list-style:none;display:flex;margin-left:99px;height:59px}
.main-nav li{font-family:"Raleway",sans-serif;font-weight:600;color:#fff;font-size:17px;padding:0 30px;line-height:59px;border-right:1px solid rgba(255,255,255,.18)}
.main-nav li.active{background:var(--navy-light)}
.main-nav li:last-child{border-right:0}

/* hero */
.hero{position:absolute;left:0;top:177px;width:1200px;height:473px;background:linear-gradient(100deg,#2b2622 0%,#4a3b30 30%,#1f2631 60%,#3d3229 80%,#23262b 100%)}
.calendar{position:absolute;left:99px;top:31px;width:499px;height:406px;background:var(--panel)}
.cal-head{display:flex;justify-content:space-between;align-items:center;padding:32px 44px 0 54px;font-family:"Raleway",sans-serif}
.cal-year{color:#e5674d;font-size:13px;font-weight:600}
.cal-month{color:#44505c;font-size:16px;font-weight:600;letter-spacing:.5px}
.cal-grid{position:absolute;left:48px;top:100px;width:410px;display:grid;grid-template-columns:repeat(7,1fr);row-gap:14px;text-align:center;font-size:12.5px;color:#333}
.cal-grid .dow{font-family:"Raleway",sans-serif;font-weight:600;font-size:15px;color:#222;padding-bottom:8px}
.cal-grid .today span{display:inline-block;width:22px;height:22px;line-height:22px;border-radius:50%;background:#e5674d;color:#fff}
.cal-arrow{position:absolute;top:225px;width:14px;height:14px;border-radius:50%;background:#e5674d}
.cal-buttons{position:absolute;left:80px;top:360px;display:flex;gap:24px}
.btn-navy{background:var(--navy);color:#fff;font-size:10.5px;font-weight:700;height:32px;line-height:32px;padding:0 28px;border-radius:2px}

.hero-news{position:absolute;left:598px;top:31px;width:503px;height:406px;background:var(--hero-panel);padding:14px 0 0 32px}
.hero-item{display:flex;gap:32px;height:124px}
.thumb-photo{flex:none}
.hero-item .thumb-photo{width:135px;height:98px}
.hero-item h4{color:#fff;font-size:12.5px;font-weight:700;margin-top:14px}
.hero-item .date{color:#e8e8e8;font-size:11.5px;margin-top:6px}
.hero-item p{color:#b9bec4;font-size:11.5px;line-height:20px;margin-top:6px;width:270px}
.scrollbar{position:absolute;right:20px;top:26px;width:6px;height:36px;background:#9aa0a6;border-radius:3px}

/* section titles */
.section-title{font-family:"Raleway",sans-serif;font-weight:700;font-size:15.5px;color:var(--navy);border-bottom:1px solid var(--line);padding-bottom:14px;width:711px}

/* tips */
.tips{position:absolute;left:99px;top:688px;width:711px}
.slider-arrows{position:absolute;right:0;top:-4px;display:flex;gap:2px}
.slider-arrows span{width:30px;height:28px;background:#eef0f2;border:1px solid #dcdfe3;display:block}
.tips-grid{display:grid;grid-template-columns:repeat(3,213px);column-gap:36px;row-gap:36px;margin-top:36px}
.tip .thumb-photo{height:142px}
.tip h4{font-size:11px;font-weight:700;color:var(--ink);line-height:21px;margin-top:14px;text-transform:uppercase}
.tip p{font-size:11px;line-height:21px;margin-top:6px}

.ad-banner{position:absolute;left:146px;top:1358px;width:624px;height:76px;background:linear-gradient(90deg,#f8f8f8,#fbe7c8 55%,#f2d5a7)}

/* events */
.events{position:absolute;left:99px;top:1469px;width:711px}
.event{position:absolute;left:0;width:711px;height:156px}
.event .thumb-photo{position:absolute;left:0;top:0;width:213px;height:156px}
.event-body{position:absolute;left:250px;top:0;width:461px}
.event h4{font-size:12.5px;font-weight:700;color:var(--ink);margin-top:2px}
.meta{display:flex;gap:22px;font-size:9.5px;color:var(--muted);margin-top:16px;padding-bottom:12px;border-bottom:1px solid var(--line);align-items:center}
.meta span{display:flex;align-items:center;gap:6px}
.event p{font-size:11px;line-height:22.5px;margin-top:10px}
.pager{position:absolute;right:0;top:1158px;display:flex;gap:6px}
.pager span{border:1px solid #d8dbdf;font-size:11px;color:#333;height:24px;line-height:22px;padding:0 9px;background:#fafafa}

/* news */
.news{position:absolute;left:99px;top:2685px;width:711px}
.news-grid{display:grid;grid-template-columns:repeat(2,330px);column-gap:51px;row-gap:40px;margin-top:44px}
.news-item h4{font-size:13px;font-weight:700;color:var(--ink);line-height:24px;text-transform:uppercase}
.news-item .rule{width:46px;height:3px;background:var(--orange);margin:10px 0 14px}
.news-item p{font-size:11.5px;line-height:23px}

/* sidebar */
.sidebar{position:absolute;left:845px;top:692px;width:256px}
.promo{height:128px;background:var(--navy);padding:16px 20px;color:#fff;position:relative;margin-bottom:18px}
.promo h5{font-family:"Raleway",sans-serif;font-weight:700;font-size:13px;line-height:20px;margin-left:46px}
.promo p{font-size:11.5px;margin-top:10px}
.promo strong{color:var(--orange);font-size:14px}
.promo svg{position:absolute;left:20px;top:18px}
.side-title{font-family:"Raleway",sans-serif;font-weight:700;font-size:15px;color:var(--navy);padding-bottom:12px;border-bottom:1px solid var(--line)}
.social-note{font-size:10.5px;margin-top:12px}
.social{display:flex;gap:6px;margin-top:20px}
.social span{width:26px;height:26px;border-radius:50%;display:block}
.card{position:relative;height:236px;margin-top:20px}
.card .thumb-photo{position:absolute;inset:0}
.card-label{position:absolute;left:0;bottom:0;width:196px;height:72px;background:rgba(18,60,105,.92);color:#fff;padding:14px 20px}
.card-label h5{font-size:11px;font-weight:700}
.card-label p{font-size:10px;margin-top:6px;font-style:italic}
.side-ad{height:213px;margin-top:20px;background:linear-gradient(160deg,#1d4f9a,#2f74c6 50%,#c9d9ee)}
.videos{display:grid;grid-template-columns:repeat(3,80px);gap:8px;margin-top:16px}
.video{height:80px;position:relative;border:1px solid #cfd3d8}
.video .thumb-photo{position:absolute;inset:3px}
.play{position:absolute;left:26px;top:27px;width:26px;height:26px;border-radius:50%;background:rgba(255,255,255,.9)}
.play::after{content:"";position:absolute;left:10px;top:7px;border-left:9px solid #333;border-top:6px solid transparent;border-bottom:6px solid transparent}
.btn-orange{background:var(--orange);color:#fff;font-size:10px;font-weight:700;text-align:center;height:38px;line-height:38px;width:163px;margin-top:24px;border-radius:2px}
.tweets{margin-top:20px;border:1px solid #d6dade;height:456px;position:relative;padding:14px 12px}
.tweets-head{display:flex;justify-content:space-between;align-items:center;font-weight:700;font-size:15px;color:var(--ink);border-bottom:1px solid var(--line);padding-bottom:10px}
.follow-btn{font-size:9px;font-weight:600;color:#333;border:1px solid #c7ccd1;background:#f3f4f5;padding:2px 8px;border-radius:3px}
.tweet{display:flex;gap:20px;padding:12px 0;border-bottom:1px solid var(--line);height:92px}
.avatar{width:64px;height:64px;background:var(--orange);color:#fff;font-size:11px;line-height:15px;text-align:center;padding-top:17px;flex:none}
.tweet p{font-size:9.5px;line-height:16px;color:#333}
.tweet p b{font-weight:700}
.tweet-actions{display:flex;gap:8px;margin-top:4px;justify-content:flex-end;margin-right:16px}
.tweet-actions i{width:9px;height:8px;background:#9aa0a6;display:block}
.tweet-box{position:absolute;left:6px;bottom:6px;right:6px;height:24px;border:1px solid #cfd3d8;font-size:9px;padding:5px 8px;color:#888}
.side-ad2{height:213px;margin-top:26px;background:linear-gradient(170deg,#3d73c8,#6fa2e0 45%,#f2d05a 80%,#e59a2a)}

/* footer */
.site-footer{position:absolute;left:0;top:3208px;width:1200px;height:269px;background:linear-gradient(180deg,#113a66,#1b5287)}
.foot-col{position:absolute;top:50px;color:#fff}
.foot-col h3{font-family:"Raleway",sans-serif;font-weight:500;font-size:21px}
.foot-col ul{list-style:none;margin-top:12px}
.foot-col li{font-size:12.5px;line-height:24px;color:#e6ecf3}
.foot-col p{font-size:12.5px;line-height:20px;color:#e6ecf3}
.email-field{width:263px;height:34px;background:#f5f6f7;margin-top:14px;display:flex;align-items:center;gap:8px;padding-left:10px;font-size:11px;color:#8a9096}
.foot-sub{width:120px;height:38px;line-height:38px;text-align:center;background:var(--orange);color:#fff;font-size:14px;margin-top:10px}
.foot-arrows{position:absolute;right:0;top:6px;font-size:15px;color:#fff;letter-spacing:8px}
.foot-follow li{font-size:11px;line-height:17px;margin-bottom:14px}
.site-bottom{position:absolute;left:0;top:3477px;width:1200px;height:66px;background:var(--navy-dark);color:#b6c3d1;font-size:12px;padding:27px 0 0 109px}
</style>
</head>
<body>

<header class="site-header">
  <div class="brand">
    <div class="brand-name">Rounds Plaza Diary</div>
    <div class="brand-tag">We are an online diary/calendar and a resource for networking events</div>
  </div>
  <div class="search-btn">
    <svg width="34" height="34" viewBox="0 0 34 34"><circle cx="16" cy="16" r="5" fill="none" stroke="#555" stroke-width="1.6"/><line x1="19.5" y1="19.5" x2="23" y2="23" stroke="#555" stroke-width="1.6"/></svg>
  </div>
  <a class="top-link" style="left:640px">Subscribe to our Weekly Bulletin</a>
  <a class="top-link" style="left:857px">Register to Add Events</a>
  <a class="login">LOGIN</a>
</header>

<nav class="main-nav">
  <ul>
    <li class="active">HOME</li><li>LATEST NEWS</li><li>UPCOMING EVENT</li><li>OUR DIARY</li><li>CALENDAR</li><li>BLOG</li><li>CONTACT</li>
  </ul>
</nav>

<section class="hero" role="img" aria-label="Blurred evening city lights behind the calendar">
  <div class="calendar">
    <div class="cal-head"><span class="cal-year">2015</span><span class="cal-month">DECEMBER, 2015</span><span class="cal-year">2016</span></div>
    <div class="cal-grid">
      <span class="dow">SUN</span><span class="dow">MON</span><span class="dow">TUE</span><span class="dow">WED</span><span class="dow">THUR</span><span class="dow">FRI</span><span class="dow">SAT</span>
      <span></span><span></span><span>1</span><span>2</span><span>3</span><span>4</span><span>5</span>
      <span>6</span><span class="today"><span>7</span></span><span>8</span><span>9</span><span>10</span><span>11</span><span>12</span>
      <span>13</span><span>14</span><span>15</span><span>16</span><span>17</span><span>18</span><span>19</span>
      <span>20</span><span>21</span><span>22</span><span>23</span><span>24</span><span>25</span><span>26</span>
      <span>27</span><span>28</span><span>29</span><span>30</span><span>31</span><span></span><span></span>
    </div>
    <span class="cal-arrow" style="left:26px"></span>
    <span class="cal-arrow" style="left:459px"></span>
    <div class="cal-buttons"><a class="btn-navy">SEE PLANED EVENTS</a><a class="btn-navy">VIEW ALL EVENTS</a></div>
  </div>
  <div class="hero-news">
    <span class="scrollbar"></span>
    <div class="hero-item">
      <div class="thumb-photo" role="img" aria-label="Photo of people meeting outdoors" style="background:linear-gradient(135deg,#b9c9d8,#8c6a55)"></div>
      <div><h4>LOREM IPSUM IS SIMPLY DUMMY TEXT</h4><div class="date">Posted on 09 December 2015</div><p>Lorem Ipsum is simply dummy text of the printing and typesetting industry.</p></div>
    </div>
    <div class="hero-item">
      <div class="thumb-photo" role="img" aria-label="Photo of a business meeting" style="background:linear-gradient(135deg,#e8eef4,#8aa4c0)"></div>
      <div><h4>LOREM IPSUM IS SIMPLY DUMMY TEXT</h4><div class="date">Posted on 09 December 2015</div><p>Lorem Ipsum is simply dummy text of the printing and typesetting industry.</p></div>
    </div>
    <div class="hero-item">
      <div class="thumb-photo" role="img" aria-label="Photo of a man at sea" style="background:linear-gradient(180deg,#d9e8f5,#3f7fb8)"></div>
      <div><h4>LOREM IPSUM IS SIMPLY DUMMY TEXT</h4><div class="date">Posted on 09 December 2015</div><p>Lorem Ipsum is simply dummy text of the printing and typesetting industry.</p></div>
    </div>
  </div>
</section>

<section class="tips">
  <h2 class="section-title">NETWORKING TIPS</h2>
  <div class="slider-arrows"><span></span><span></span></div>
  <div class="tips-grid">
    <article class="tip"><div class="thumb-photo" role="img" aria-label="Photo of a busy city square" style="background:linear-gradient(180deg,#c7ccd2,#6d6660)"></div><h4>Lorem Ipsum is simply dummy text of the printing</h4><p>Lorem Ipsum is simply dummy text of the printing and typesetting industry. been the industry's...</p></article>
    <article class="tip"><div class="thumb-photo" role="img" aria-label="Photo of a figure on a pier at sunset" style="background:linear-gradient(180deg,#d8d8d8,#4a4a4a)"></div><h4>Lorem Ipsum is simply dummy text of the printing</h4><p>Lorem Ipsum is simply dummy text of the printing and typesetting industry. been the industry's...</p></article>
    <article class="tip"><div class="thumb-photo" role="img" aria-label="Photo of an escalator hall" style="background:linear-gradient(180deg,#e0e0e0,#7b7b7b)"></div><h4>Lorem Ipsum is simply dummy text of the printing</h4><p>Lorem Ipsum is simply dummy text of the printing and typesetting industry. been the industry's...</p></article>
    <article class="tip"><div class="thumb-photo" role="img" aria-label="Photo of a car dashboard on the road" style="background:linear-gradient(180deg,#8fa2b5,#2a2d31)"></div><h4>Lorem Ipsum is simply dummy text of the printing</h4><p>Lorem Ipsum is simply dummy text of the printing and typesetting industry. been the industry's...</p></article>
    <article class="tip"><div class="thumb-photo" role="img" aria-label="Photo of an airliner in flight" style="background:linear-gradient(180deg,#5f84b8,#dce5ef)"></div><h4>Lorem Ipsum is simply dummy text of the printing</h4><p>Lorem Ipsum is simply dummy text of the printing and typesetting industry. been the industry's...</p></article>
    <article class="tip"><div class="thumb-photo" role="img" aria-label="Photo of a passport on a world map" style="background:linear-gradient(135deg,#6b4a2e,#b88a52)"></div><h4>Lorem Ipsum is simply dummy text of the printing</h4><p>Lorem Ipsum is simply dummy text of the printing and typesetting industry. been the industry's...</p></article>
  </div>
</section>

<div class="ad-banner" role="img" aria-label="Advertisement banner for free video tutorials"></div>

<section class="events">
  <h2 class="section-title">UPCOMING EVENTS</h2>
  <article class="event" style="top:73px">
    <div class="thumb-photo" role="img" aria-label="Photo of a historic waterfront city" style="background:linear-gradient(180deg,#a9c3dc,#9a7a5a)"></div>
    <div class="event-body"><h4>LOREM IPSUM IS SIMPLY DUMMY EXT OF THE PRINTING</h4>
      <div class="meta"><span>◷ 27 MARCH 2015</span><span>▭ 128</span><span>◉ 300</span></div>
      <p>Lorem Ipsum is simply dummy text of the printing and typesetting industry. Lorem Ipsum has been the industry's standard dummy text ever since the 1500s, when an unknown printer took a galley of type and scrambled it to make a type specimen book. It has survived not only five centuries, but also the leap...</p></div>
  </article>
  <article class="event" style="top:295px">
    <div class="thumb-photo" role="img" aria-label="Photo of a high-speed train" style="background:linear-gradient(135deg,#d4d8dc,#6b3a3a)"></div>
    <div class="event-body"><h4>LOREM IPSUM IS SIMPLY DUMMY EXT OF THE PRINTING</h4>
      <div class="meta"><span>◷ 27 MARCH 2015</span><span>▭ 128</span><span>◉ 300</span></div>
      <p>Lorem Ipsum is simply dummy text of the printing and typesetting industry. Lorem Ipsum has been the industry's standard dummy text ever since the 1500s, when an unknown printer took a galley of type and scrambled it to make a type specimen book. It has survived not only five centuries, but also the leap...</p></div>
  </article>
  <article class="event" style="top:515px">
    <div class="thumb-photo" role="img" aria-label="Photo of colleagues at a laptop" style="background:linear-gradient(135deg,#cfc6b8,#7d6e5e)"></div>
    <div class="event-body"><h4>LOREM IPSUM IS SIMPLY DUMMY EXT OF THE PRINTING</h4>
      <div class="meta"><span>◷ 27 MARCH 2015</span><span>▭ 128</span><span>◉ 300</span></div>
      <p>Lorem Ipsum is simply dummy text of the printing and typesetting industry. Lorem Ipsum has been the industry's standard dummy text ever since the 1500s, when an unknown printer took a galley of type and scrambled it to make a type specimen book. It has survived not only five centuries, but also the leap...</p></div>
  </article>
  <article class="event" style="top:737px">
    <div class="thumb-photo" role="img" aria-label="Photo of two people talking" style="background:linear-gradient(135deg,#5b6f80,#2b2f35)"></div>
    <div class="event-body"><h4>LOREM IPSUM IS SIMPLY DUMMY EXT OF THE PRINTING</h4>
      <div class="meta"><span>◷ 27 MARCH 2015</span><span>▭ 128</span><span>◉ 300</span></div>
      <p>Lorem Ipsum is simply dummy text of the printing and typesetting industry. Lorem Ipsum has been the industry's standard dummy text ever since the 1500s, when an unknown printer took a galley of type and scrambled it to make a type specimen book. It has survived not only five centuries, but also the leap...</p></div>
  </article>
  <article class="event" style="top:959px">
    <div class="thumb-photo" role="img" aria-label="Photo of a surprised man in glasses" style="background:linear-gradient(135deg,#f0e2c8,#c24a3a)"></div>
    <div class="event-body"><h4>LOREM IPSUM IS SIMPLY DUMMY EXT OF THE PRINTING</h4>
      <div class="meta"><span>◷ 27 MARCH 2015</span><span>▭ 128</span><span>◉ 300</span></div>
      <p>Lorem Ipsum is simply dummy text of the printing and typesetting industry. Lorem Ipsum has been the industry's standard dummy text ever since the 1500s, when an unknown printer took a galley of type and scrambled it to make a type specimen book. It has survived not only five centuries, but also the leap...</p></div>
  </article>
  <nav class="pager"><span>Prev</span><span>1</span><span>2</span><span>3</span><span>4</span><span>5</span><span>6</span><span>...</span><span>22</span><span>Next</span></nav>
</section>

<section class="news">
  <h2 class="section-title">NETWORKING NEWS</h2>
  <div class="news-grid">
    <article class="news-item"><h4>Lorem Ipsum is simply dummy ext<br>of the printing</h4><div class="rule"></div><p>Lorem Ipsum is simply dummy text of the printing and typesetting industry. Lorem Ipsum has been the industry's standard dummy text ever since the 1500s, when an unknown printer took a galley...</p></article>
    <article class="news-item"><h4>Lorem Ipsum is simply dummy ext<br>of the printing</h4><div class="rule"></div><p>Lorem Ipsum is simply dummy text of the printing and typesetting industry. Lorem Ipsum has been the industry's standard dummy text ever since the 1500s, when an unknown printer took a galley...</p></article>
    <article class="news-item"><h4>Lorem Ipsum is simply dummy ext<br>of the printing</h4><div class="rule"></div><p>Lorem Ipsum is simply dummy text of the printing and typesetting industry. Lorem Ipsum has been the industry's standard dummy text ever since the 1500s, when an unknown printer took a galley...</p></article>
    <article class="news-item"><h4>Lorem Ipsum is simply dummy ext<br>of the printing</h4><div class="rule"></div><p>Lorem Ipsum is simply dummy text of the printing and typesetting industry. Lorem Ipsum has been the industry's standard dummy text ever since the 1500s, when an unknown printer took a galley...</p></article>
  </div>
</section>

<aside class="sidebar">
  <div class="promo">
    <svg width="36" height="30" viewBox="0 0 36 30" fill="none" stroke="#f5a01a" stroke-width="2"><circle cx="18" cy="8" r="5"/><path d="M8 28c0-6 4-10 10-10s10 4 10 10"/><circle cx="6" cy="11" r="3.5"/><circle cx="30" cy="11" r="3.5"/></svg>
    <h5>COMMUNITY<br>EVENTS</h5>
    <p>community events and one off events would be <strong>FREE</strong></p>
  </div>
  <div class="promo">
    <svg width="30" height="34" viewBox="0 0 30 34" fill="none" stroke="#f5a01a" stroke-width="2"><rect x="4" y="2" width="22" height="30"/><path d="M10 8h3M17 8h3M10 14h3M17 14h3M10 20h3M17 20h3M13 32v-6h4v6"/></svg>
    <h5>BUSINESS AND<br>COMMERCIAL EVENTS</h5>
    <p>would be <strong>CHARGEABLE</strong></p>
  </div>
  <h3 class="side-title" style="margin-top:8px">FOLLOW US</h3>
  <p class="social-note">Connect with our social media</p>
  <div class="social" aria-label="Social media links">
    <span style="background:#3b5998"></span><span style="background:#41a9e1"></span><span style="background:#d9412f"></span><span style="background:#2d6fb0"></span><span style="background:#58a548"></span><span style="background:#2a84b8"></span><span style="background:#d63b2f"></span><span style="background:#f5a01a"></span>
  </div>
  <div class="card">
    <div class="thumb-photo" role="img" aria-label="Photo of a smiling professional" style="background:linear-gradient(135deg,#eef3f8,#9fb7cf)"></div>
    <div class="card-label"><h5>SUBSCRIBE</h5><p>Subscribe to our Event »</p></div>
  </div>
  <div class="card">
    <div class="thumb-photo" role="img" aria-label="Photo of a woman at a desk" style="background:linear-gradient(135deg,#f3f4f5,#b7bcc2)"></div>
    <div class="card-label"><h5>REGISTER</h5><p>Register to Add Events »</p></div>
  </div>
  <div class="side-ad" role="img" aria-label="Advertisement for web hosting servers"></div>
  <h3 class="side-title" style="margin-top:46px">VIDEO GALLERY</h3>
  <div class="videos">
    <div class="video"><div class="thumb-photo" role="img" aria-label="Video still of people at an event" style="background:#8aa0b6"></div><span class="play"></span></div>
    <div class="video"><div class="thumb-photo" role="img" aria-label="Video still of a beach" style="background:#6fb2d8"></div><span class="play"></span></div>
    <div class="video"><div class="thumb-photo" role="img" aria-label="Video still of a meeting" style="background:#a89886"></div><span class="play"></span></div>
    <div class="video"><div class="thumb-photo" role="img" aria-label="Video still of a conversation" style="background:#9d8c7c"></div><span class="play"></span></div>
    <div class="video"><div class="thumb-photo" role="img" aria-label="Video still of a group" style="background:#b7a896"></div><span class="play"></span></div>
    <div class="video"><div class="thumb-photo" role="img" aria-label="Video still of an office" style="background:#c4ccd4"></div><span class="play"></span></div>
  </div>
  <div class="btn-orange">VIEW MORE VIDEOS</div>
  <div class="tweets">
    <div class="tweets-head"><span>Tweets</span><span class="follow-btn">Follow</span></div>
    <div class="tweet"><div class="avatar">Rounds<br>Events</div><div><p><b>Lorem Ipsum is simply</b> dummy text of the printing and typesetting...</p><div class="tweet-actions"><i></i><i></i><i></i></div></div></div>
    <div class="tweet"><div class="avatar">Rounds<br>Events</div><div><p><b>Lorem Ipsum is simply</b> dummy text of the printing and typesetting...</p><div class="tweet-actions"><i></i><i></i><i></i></div></div></div>
    <div class="tweet"><div class="avatar">Rounds<br>Events</div><div><p><b>Lorem Ipsum is simply</b> dummy text of the printing and typesetting...</p><div class="tweet-actions"><i></i><i></i><i></i></div></div></div>
    <div class="tweet" style="border-bottom:0"><div class="avatar">Rounds<br>Events</div><div><p><b>Lorem Ipsum is simply</b> dummy text of the printing and typesetting...</p></div></div>
    <div class="tweet-box">Tweet to @roundsevents</div>
  </div>
  <div class="side-ad2" role="img" aria-label="Advertisement for a family web account offer"></div>
</aside>

<footer class="site-footer">
  <div class="foot-col" style="left:109px">
    <h3>Quick links</h3>
    <ul><li>About Us</li><li>What We Do</li><li>How we work</li><li>Blog Post</li><li>News &amp; Events</li></ul>
  </div>
  <div class="foot-col" style="left:319px">
    <h3>Resources</h3>
    <ul><li>Mauris vel lacus</li><li>Vitae felis vestibulum</li><li>Aoliutpat imperdiet</li><li>Cum sociis</li><li>Natoque penatibus</li></ul>
  </div>
  <div class="foot-col" style="left:539px">
    <h3>Newsletters Sign Up</h3>
    <p style="margin-top:8px">Please sign up here for latest news</p>
    <div class="email-field"><svg width="14" height="10" viewBox="0 0 14 10"><rect x=".5" y=".5" width="13" height="9" fill="none" stroke="#888"/><path d="M.5.5l6.5 5 6.5-5" fill="none" stroke="#888"/></svg>Email address</div>
    <div class="foot-sub">Subscribe</div>
  </div>
  <div class="foot-col foot-follow" style="left:857px;width:244px">
    <h3>Follow Us</h3>
    <span class="foot-arrows">‹ ›</span>
    <ul><li>Lorem Ipsum is simply dummy text of the http://www.presscraftstudio.com</li><li>Lorem Ipsum is simply dummy text of the http://www.presscraftstudio.com</li><li>Lorem Ipsum is simply dummy text of the http://www.presscraftstudio.com</li></ul>
  </div>
</footer>
<div class="site-bottom">© 2015 Company Name &nbsp;All right reserved &nbsp;Term of Use</div>

</body>
</html>
```